Energy cost saving website (job description rewritten!)

Job Type: WordPress design
Task Outline: Create a WordPress design
Task Description:
We are new business (Germany) in the market of saving costs by power-saving (name: 'wir-falten-eure-Wolkenbögen.de'). This is reached by changing the supplier, the use of LED bulbs, energy saving washing machines, stoves, microwaves, hairdryers, vacuum cleaners and the like - where all of these be selled or affiliated through the website maybe you will create for us.
Design parameters:
We want a serious design that embodies a feeling of honesty, competence and capability.
Visitors should particularly see that this site saves them money!
The home page mainly should act as a selector of possibilities saving money by power-saving, usage of LED bulbs and large energy saving household devices (washing machines, etc.)
Updates
Hello designers,
browsing through the PixelHarbors files of portfolios I found one header graphics which excites me. Please find it here: http://www.pixelharbor-example.net/design/482716/wordpress-design-by-tarek-olumide . Note: it is NOT the picture but the shadowing. So if you consider this in your concepts would be another 'nice-to-have'.
Thanks.
Target Market(s)
People looking out for saving money by power-saving.
Industry/Entity Type
Business
Requirements
Must have
- Look and feel of 'this site saves me money'!
Nice to have
- We love 3D effects, but its not a must have. We also like cartoons, but feel free to develop your own concept, please. An appropriate backgrond picture would be nice.
Should not have
- Some kind of these exaggerated smiling or handshaking photos. That bathetic symbols like money bills or coins stacks.

```html
<!DOCTYPE html>
<html lang="en">
<head>
<meta charset="utf-8">
<title>BrightVolt – Power Saving Equipements</title>
<link href="https://fonts.googleapis.com/css2?family=Arvo:wght@700&family=Open+Sans:wght@400;600;700&family=Oswald:wght@500&family=Titillium+Web:ital,wght@0,400;0,600;1,400&family=Rosarivo&display=swap" rel="stylesheet">
<style>
:root{
  --green:#4cc234;
  --green-text:#3bab27;
  --orange:#ff7a00;
  --orange-light:#ff9a2e;
  --ink:#333;
  --muted:#8a8a8a;
  --olive:#8a6d1f;
  --hero-bg:#f4f4f4;
  --section-bg:#e9eaed;
  --panel:#ffffff;
  --box:#f1f2f4;
  --footer:#3a3a3a;
  --footer-text:#e6e6e6;
  --footer-head:#9a9a9a;
}
*{margin:0;padding:0;box-sizing:border-box}
html,body{width:934px;height:1200px;overflow:hidden}
body{position:relative;background:var(--section-bg);font-family:"Open Sans",sans-serif;color:var(--ink)}
.abs{position:absolute}
.hero{left:0;top:0;width:934px;height:365px;background:var(--hero-bg);border-bottom:1px solid #ddd}
.navbar{left:102px;top:42px;width:730px;height:37px;background:linear-gradient(#5fd43f,#43b82a);border-radius:2px;box-shadow:0 8px 8px -6px rgba(0,0,0,.35)}
.navbar a{position:absolute;top:11px;color:#fff;font-weight:700;font-size:10px;text-decoration:none;white-space:nowrap}
.logo-bubble{left:362px;top:-10px;width:182px;height:102px;background:radial-gradient(ellipse at 50% 30%,#fff 55%,#e8f7d8);border-radius:0 0 91px 91px;border:2px solid #bfe9a6;border-top:none}
.logo-bubble::after{content:"";position:absolute;left:85px;bottom:-7px;width:10px;height:10px;background:#f0f9e6;transform:rotate(45deg);border-right:2px solid #bfe9a6;border-bottom:2px solid #bfe9a6}
.logo{left:367px;top:22px;width:172px;text-align:center;font-family:"Open Sans",sans-serif;font-weight:700;font-size:24px;color:#2a2a2a;white-space:nowrap}
.logo .dot{display:inline-block;width:16px;height:16px;background:var(--green);border-radius:3px;margin-right:5px;vertical-align:-1px}
.basket{left:610px;top:15px;font-size:9px;font-weight:700;color:var(--green-text);white-space:nowrap}
.basket span{color:#333;font-weight:400;margin-left:6px}
.hero-img{left:152px;top:128px;width:256px;height:184px;background:radial-gradient(ellipse at 45% 45%,#ffffff 25%,#d4d8dc 60%,transparent 72%)}
.headline{left:450px;top:122px;font-family:"Arvo",serif;font-size:41px;color:var(--green-text);letter-spacing:1px;white-space:nowrap}
.subhead{left:450px;top:166px;font-family:"Titillium Web",sans-serif;font-size:18px;color:#444;white-space:nowrap}
.benefits{left:456px;top:200px;width:218px;list-style:none}
.benefits li{height:22px;line-height:20px;border-bottom:1px solid #ddd;font-family:"Titillium Web",sans-serif;font-style:italic;font-size:12px;color:var(--green-text);padding-left:15px;position:relative;white-space:nowrap}
.benefits li::before{content:"";position:absolute;left:2px;top:7px;width:7px;height:7px;background:var(--green);border-radius:50%}
.btn-browse{left:462px;top:302px;width:204px;height:42px;background:linear-gradient(var(--orange-light),var(--orange));border-radius:3px;text-align:center;color:#fff}
.btn-browse b{display:block;font-family:"Titillium Web",sans-serif;font-size:20px;font-weight:600;line-height:22px;margin-top:5px;letter-spacing:.5px}
.btn-browse small{display:block;font-size:6px;font-style:italic;color:#ffe3b8;white-space:nowrap}
.range-title{left:0;width:934px;top:386px;text-align:center;font-family:"Rosarivo",serif;font-weight:400;font-size:30px;color:#333;white-space:nowrap}
.tile{width:228px;height:74px;background:#fff;padding:3px;box-shadow:0 1px 3px rgba(0,0,0,.2)}
.tile .img{width:100%;height:100%}
.tile .label{position:absolute;background:#000;font-family:"Titillium Web",sans-serif;font-weight:600;font-size:14px;padding:3px 5px;white-space:nowrap;line-height:20px}
.panel{left:102px;top:637px;width:732px;height:427px;background:var(--panel)}
.products{left:116px;top:650px;width:496px;height:400px;background:var(--box);border:1px solid #d9dadd}
.product{width:100px}
.product .thumb{width:100px;height:68px;border:3px solid #fff;box-shadow:0 0 2px rgba(0,0,0,.2);background:radial-gradient(circle at 35% 50%,#f4f4f4 30%,#d8d8d8 45%,#17962e 47%,#0f7a25)}
.product h4{margin-top:12px;font-size:9.5px;font-weight:600;color:#555;text-decoration:underline;padding-left:4px}
.product p{font-size:7px;color:var(--muted);line-height:10px;padding-left:4px;margin-top:4px}
.product .price{font-size:10px;font-weight:700;padding-left:7px;margin-top:6px;color:#111}
.product .price big{font-size:17px}
.product .add{margin:6px 0 0 25px;width:49px;height:19px;background:var(--orange);border-radius:2px;color:#fff;font-size:9px;font-weight:700;line-height:19px;padding-left:7px;white-space:nowrap}
.product .add i{display:inline-block;width:12px;font-style:normal;border-right:1px solid #ffb066;margin-right:8px}
.cat-title{left:620px;top:654px;font-family:"Oswald",sans-serif;font-weight:500;font-size:21px;color:#222}
.cat-line{left:612px;top:686px;width:208px;height:32px;background:#eceef3;border:1px solid #dcdfe6;border-left:none}
.cats{left:620px;top:696px;list-style:none}
.cats li{height:27.8px;font-size:9px;color:var(--olive);padding-left:12px;position:relative;white-space:nowrap}
.cats li::before{content:"";position:absolute;left:2px;top:5px;width:3px;height:3px;border-radius:50%;background:var(--olive)}
.cats li.active{color:#666}
.cats li.active::before{background:#999}
.ad{left:623px;top:873px;width:199px;height:173px;background:#6d6d6d;border:1px solid #888;color:#fff;text-align:center;font-family:"Open Sans",sans-serif;font-weight:700}
.ad .t1{margin-top:50px;font-size:17px}
.ad .t2{font-size:38px;line-height:46px}
.footer{left:0;top:1088px;width:934px;height:112px;background:var(--footer)}
.f-head{top:1104px;font-family:"Titillium Web",sans-serif;font-size:13px;color:var(--footer-head)}
.f-links{top:1127px;list-style:none;font-size:8.5px;color:var(--footer-text)}
.f-links li{height:16px;white-space:nowrap}
.cards{left:446px;top:1129px;white-space:nowrap}
.cards span{display:inline-block;height:16px;border:1px solid #ccc;background:#f5f5f5;color:#333;font-size:7px;font-weight:700;line-height:14px;padding:0 3px;margin-right:1px}
.contact{left:644px;top:1104px;font-size:8.5px;color:var(--footer-text)}
.contact div{height:23px;display:flex;align-items:center;white-space:nowrap}
.contact svg{width:18px;height:14px;margin-right:15px}
.copy{left:646px;top:1175px;font-size:8.5px;color:#bbb;white-space:nowrap}
</style>
</head>
<body>
<div class="abs hero"></div>
<nav class="abs navbar">
  <a style="left:18px">HOME</a><a style="left:67px">ABOUT</a><a style="left:121px">CONTACT US</a>
  <a style="left:528px">PRODUCTS</a><a style="left:600px">LOGIN</a><a style="left:649px">REGISTER</a>
</nav>
<div class="abs logo-bubble"></div>
<div class="abs logo"><span class="dot"></span>BrightVolt</div>
<div class="abs basket">YOUR SHOPPING BASEKT
  <svg width="16" height="13" viewBox="0 0 16 13" style="vertical-align:-3px;margin-left:10px"><path d="M1 4h14l-2 8H3z M5 4l3-3 3 3" fill="none" stroke="#555" stroke-width="1.5"/></svg>
  <span>0 &nbsp;|&nbsp; $00.00</span></div>

<div class="abs hero-img" role="img" aria-label="White LED light bulb lying on its side"></div>
<h1 class="abs headline">SAVE COSTS BY</h1>
<div class="abs subhead">POWER SAVING EQUIPEMENTS</div>
<ul class="abs benefits">
  <li>Save Power by 30%</li><li>Get Modern and decorative Looks</li><li>Low COSTS</li><li>Better Results</li>
</ul>
<div class="abs btn-browse"><b>BROWSE ALL</b><small>COMPLETE RANGE OF POSER SAVING EQUIPEMENTS</small></div>

<h2 class="abs range-title">Range Of Our Power-Saving Equipements</h2>

<div class="abs tile" style="left:116px;top:442px"><div class="img" role="img" aria-label="LED bulb photo" style="background:linear-gradient(90deg,#f3efd8,#e8e4c8 45%,#3a3a3a 70%,#9a9a9a)"></div><span class="label" style="left:6px;top:14px;color:#f3df3a">LED BULBS</span></div>
<div class="abs tile" style="left:354px;top:442px"><div class="img" role="img" aria-label="Washing machines photo" style="background:linear-gradient(90deg,#c9d6e6,#9fb3cc 40%,#dfe6ef)"></div><span class="label" style="left:112px;top:26px;color:#e8e8e8;font-size:13px;padding:5px 2px 5px 3px">WASHING MACHINE</span></div>
<div class="abs tile" style="left:590px;top:442px"><div class="img" role="img" aria-label="Stove photo on green background" style="background:linear-gradient(90deg,#4aa83a,#3b3b3b 40%,#5a5a5a 80%,#4aa83a)"></div><span class="label" style="left:3px;top:14px;color:#8de04a;padding:5px 88px 5px 5px">STOVES</span></div>
<div class="abs tile" style="left:116px;top:526px"><div class="img" role="img" aria-label="Microwave photo" style="background:linear-gradient(90deg,#8c8f94,#d4d6d9 45%,#2a2a2a)"></div><span class="label" style="left:110px;top:30px;color:#ff2f5a;padding:5px 7px">MICROWAVES</span></div>
<div class="abs tile" style="left:354px;top:526px"><div class="img" role="img" aria-label="Hand dryer photo" style="background:linear-gradient(90deg,#d8dadc,#f4f4f4 40%,#1f1f1f 60%,#c9c9c9)"></div><span class="label" style="left:104px;top:31px;color:#4bb4ff;padding:5px 10px">HAND DRYERS</span></div>
<div class="abs tile" style="left:590px;top:526px"><div class="img" role="img" aria-label="Vacuum cleaner photo" style="background:linear-gradient(90deg,#1e2226,#58606a 50%,#2a2f35)"></div><span class="label" style="left:3px;top:8px;color:#f3df3a;padding:5px 10px">VACUUM CLEANERS</span></div>

<div class="abs panel"></div>
<div class="abs products"></div>
<div class="abs product" style="left:132px;top:670px"><div class="thumb" role="img" aria-label="LED bulb on green"></div><h4>Led Bulbs</h4><p>Lorem ipsum dolor site amet. this is the test...</p><div class="price">$<big>12</big>.99</div><div class="add"><i>+</i>Add</div></div>
<div class="abs product" style="left:252px;top:670px"><div class="thumb" role="img" aria-label="LED bulb on green"></div><h4>Led Bulbs</h4><p>Lorem ipsum dolor site amet. this is the test...</p><div class="price">$<big>12</big>.99</div><div class="add"><i>+</i>Add</div></div>
<div class="abs product" style="left:373px;top:670px"><div class="thumb" role="img" aria-label="LED bulb on green"></div><h4>Led Bulbs</h4><p>Lorem ipsum dolor site amet. this is the test...</p><div class="price">$<big>12</big>.99</div><div class="add"><i>+</i>Add</div></div>
<div class="abs product" style="left:494px;top:670px"><div class="thumb" role="img" aria-label="LED bulb on green"></div><h4>Led Bulbs</h4><p>Lorem ipsum dolor site amet. this is the test...</p><div class="price">$<big>12</big>.99</div><div class="add"><i>+</i>Add</div></div>
<div class="abs product" style="left:132px;top:858px"><div class="thumb" role="img" aria-label="LED bulb on green"></div><h4>Led Bulbs</h4><p>Lorem ipsum dolor site amet. this is the test...</p><div class="price">$<big>12</big>.99</div><div class="add"><i>+</i>Add</div></div>
<div class="abs product" style="left:252px;top:858px"><div class="thumb" role="img" aria-label="LED bulb on green"></div><h4>Led Bulbs</h4><p>Lorem ipsum dolor site amet. this is the test...</p><div class="price">$<big>12</big>.99</div><div class="add"><i>+</i>Add</div></div>
<div class="abs product" style="left:373px;top:858px"><div class="thumb" role="img" aria-label="LED bulb on green"></div><h4>Led Bulbs</h4><p>Lorem ipsum dolor site amet. this is the test...</p><div class="price">$<big>12</big>.99</div><div class="add"><i>+</i>Add</div></div>
<div class="abs product" style="left:494px;top:858px"><div class="thumb" role="img" aria-label="LED bulb on green"></div><h4>Led Bulbs</h4><p>Lorem ipsum dolor site amet. this is the test...</p><div class="price">$<big>12</big>.99</div><div class="add"><i>+</i>Add</div></div>

<h3 class="abs cat-title">CATEGORIES</h3>
<div class="abs cat-line"></div>
<ul class="abs cats">
  <li class="active">LED bulbs</li><li>Washing maChines</li><li>Stoves</li><li>Microwaves</li><li>Hairdryers</li><li>Vacuum Cleaners</li>
</ul>
<div class="abs ad"><div class="t1">Advertisement</div><div class="t2">Space</div></div>

<footer class="abs footer"></footer>
<div class="abs f-head" style="left:104px">Customer Service</div>
<ul class="abs f-links" style="left:108px"><li>Order Status</li><li>Shipping Information</li><li>Returns &amp; Exchanges</li><li>Sales &amp; Coupons</li></ul>
<div class="abs f-head" style="left:275px">Our Company</div>
<ul class="abs f-links" style="left:276px"><li>Contact us</li><li>About us</li><li>Terms &amp; Conditions</li><li>Privacy</li></ul>
<div class="abs f-head" style="left:446px">We accept</div>
<div class="abs cards"><span>Trelvo</span><span>Kandri</span><span>Mosbel</span><span>Vintari</span><span>Quolap</span></div>
<div class="abs contact">
  <div><svg viewBox="0 0 18 14"><rect x="1" y="2" width="16" height="10" fill="none" stroke="#fff" stroke-width="1.4"/><path d="M1 2l8 6 8-6" fill="none" stroke="#fff" stroke-width="1.4"/></svg>ges of Lorem Ipsum There.</div>
  <div><svg viewBox="0 0 18 14"><path d="M1 2h3l2 8h9l2-6H5" fill="none" stroke="#fff" stroke-width="1.4"/><circle cx="7" cy="12.5" r="1.2" fill="#fff"/><circle cx="14" cy="12.5" r="1.2" fill="#fff"/></svg>Place An Order &nbsp; 0-0000-000-0000</div>
  <div><svg viewBox="0 0 18 14"><circle cx="9" cy="4" r="3" fill="#fff"/><path d="M3 14c0-4 3-6 6-6s6 2 6 6z" fill="#fff"/><circle cx="3.5" cy="6" r="2" fill="#fff"/><circle cx="14.5" cy="6" r="2" fill="#fff"/></svg>Customer Service &nbsp; 0-000-000-0000</div>
</div>
<div class="abs copy">© 2012 &nbsp;copyright All Right Reserved</div>
</body>
</html>
```